Brightstep Foot Care Advertisement Sandwich board

We need a Sandwich board design for our fungal nail clinic - please find attached the sandwich board dimensions.

The sandwich board itself will be displayed outside of a large health clinic and we need it to attract the attention of people walking by. We need a brochure holder included in the design which will hold our brochures which provides as clients with more information (please see attached also).

We are open to the designers creativity but we would like a similar theme portrayed on our board that is similar to our website (www.brightstepfootcare.co.nz) and brochure that incorporates our logo which I have attached). The final design should communicate professionalism and be a minimalist look but modern to capture the attention of pedestrians.

Finally, we would like the website and phone number (07) 312 5840.

We look forward to seeing your work.

```html
<!DOCTYPE html>
<html lang="en">
<head>
<meta charset="utf-8">
<title>Brightstep Foot Care – Sandwich Board</title>
<link rel="stylesheet" href="https://fonts.googleapis.com/css2?family=Montserrat:wght@600;700;800&display=swap">
<style>
  :root {
    --page: #e2e2e2;
    --white: #ffffff;
    --brand-blue: #3a66b4;
    --navy: #1c3b7a;
    --ink: #1a1a1a;
    --grey-text: #6b6b6b;
    --grey-band: #b5b5b5;
    --mist: #e9eef7;
    --skin-light: #f3d2bf;
    --skin-mid: #e8b79c;
  }
  * { margin: 0; padding: 0; box-sizing: border-box; }
  html, body { width: 935px; height: 1200px; overflow: hidden; }
  body {
    background: var(--page);
    font-family: "Montserrat", Arial, sans-serif;
    position: relative;
  }
  .board {
    position: absolute;
    left: 66px; top: 64px;
    width: 805px; height: 1074px;
    overflow: hidden;
    background:
      linear-gradient(115deg, var(--mist) 0%, var(--white) 18%, var(--mist) 30%, var(--white) 45%, var(--white) 100%);
    box-shadow: 0 4px 14px rgba(0,0,0,0.25);
  }
  .hero-photo {
    position: absolute;
    left: 450px; top: 0;
    width: 355px; height: 830px;
    border-radius: 0 0 0 180px;
    background: linear-gradient(160deg, var(--skin-light) 0%, var(--skin-mid) 55%, var(--skin-light) 100%);
    opacity: 0.85;
  }
  .handle-slot {
    position: absolute;
    left: 292px; top: 54px;
    width: 220px; height: 42px;
    border-radius: 21px;
    background: var(--page);
    box-shadow: inset 0 2px 5px rgba(0,0,0,0.3);
  }
  .brand {
    position: absolute;
    left: 55px; top: 58px;
    width: 265px;
    text-align: center;
  }
  .brand-mark {
    width: 96px; height: 96px;
    margin: 0 auto 22px;
    border-radius: 50%;
    background: var(--brand-blue);
  }
  .brand-name {
    font-weight: 700;
    font-size: 22px;
    letter-spacing: 1.5px;
    color: var(--ink);
    text-transform: uppercase;
  }
  .headline {
    position: absolute;
    left: 50px; top: 248px;
    font-weight: 800;
    line-height: 1;
    text-transform: uppercase;
  }
  .headline span { display: block; }
  .headline .line-your { font-size: 88px; color: var(--grey-text); height: 80px; }
  .headline .line-fungal { font-size: 88px; color: var(--brand-blue); height: 78px; }
  .headline .line-nail { font-size: 166px; color: var(--brand-blue); height: 142px; letter-spacing: -2px; }
  .headline .line-experts { font-size: 72px; color: var(--grey-text); }
  .waves { position: absolute; left: 0; top: 0; }
  .brochure-holder {
    position: absolute;
    left: 52px; top: 753px;
    width: 145px; height: 282px;
    background: linear-gradient(90deg, #dcdcdc 0%, #ffffff 18%, #f4f4f4 60%, #d8d8d8 100%);
    border: 3px solid #efefef;
    box-shadow: 0 1px 4px rgba(0,0,0,0.2);
  }
  .contact {
    position: absolute;
    left: 226px; top: 848px;
    color: var(--white);
    font-weight: 700;
  }
  .contact .cta { font-size: 56px; line-height: 1; letter-spacing: 0.5px; }
  .contact .phone { font-size: 74px; line-height: 1; margin-top: 10px; }
  .contact .web {
    display: flex; align-items: center; gap: 18px;
    margin-top: 16px;
    font-size: 26px;
  }
  .contact .web svg { width: 34px; height: 34px; }
</style>
</head>
<body>
  <div class="board">
    <div class="hero-photo" role="img" aria-label="Photo of a woman's smooth bare legs and feet standing on tiptoe, her hand resting on her calf"></div>

    <svg class="waves" width="805" height="1074" viewBox="0 0 805 1074" aria-hidden="true">
      <path fill="var(--navy)" d="M0 605 C140 690 290 720 440 692 C560 668 650 640 730 650 C770 658 805 690 805 700 L805 1074 L0 1074 Z"/>
      <path fill="var(--grey-band)" d="M0 640 C140 712 300 740 450 712 C560 690 640 630 740 638 C775 642 800 670 805 690 L805 1074 L0 1074 Z"/>
      <path fill="var(--ink)" d="M0 650 C150 730 310 760 460 728 C570 705 650 652 740 660 C780 665 805 700 805 720 L805 1074 L0 1074 Z"/>
      <path fill="var(--brand-blue)" d="M0 660 C160 748 320 772 470 740 C580 716 650 672 730 678 C770 682 805 720 805 740 L805 1074 L0 1074 Z"/>
      <path fill="var(--navy)" d="M640 690 C720 680 790 740 805 800 L805 680 Z" opacity="0.9"/>
    </svg>

    <div class="handle-slot"></div>

    <div class="brand">
      <div class="brand-mark"></div>
      <div class="brand-name">Brightstep Foot Care</div>
    </div>

    <h1 class="headline">
      <span class="line-your">Your</span>
      <span class="line-fungal">Fungal</span>
      <span class="line-nail">Nail</span>
      <span class="line-experts">Experts</span>
    </h1>

    <div class="brochure-holder"></div>

    <div class="contact">
      <div class="cta">CALL US NOW</div>
      <div class="phone">(07) 312 5840</div>
      <div class="web">
        <svg viewBox="0 0 34 34" aria-hidden="true" fill="none" stroke="#fff" stroke-width="2.4">
          <circle cx="17" cy="17" r="15"/>
          <ellipse cx="17" cy="17" rx="6.5" ry="15"/>
          <line x1="2" y1="17" x2="32" y2="17"/>
          <line x1="5" y1="9" x2="29" y2="9"/>
          <line x1="5" y1="25" x2="29" y2="25"/>
        </svg>
        <span>www.brightstepfootcare.co.nz</span>
      </div>
    </div>
  </div>
</body>
</html>
```